Heritage Hollow Business Cards

Require a business card design. <br/><br/>Needs to include logo (either round or long version) plus these details:<br/>Maya Torvel<br/>Heritage Hollow<br/>maya@quonbrook.com.au<br/>02 6481 7390<br/>PO Box Glenwarra NSW 2913<br/>www.heritagehollow.com.au<br/><br/>I need in an editable format so that I can create for multiple staff members. <br/><br/>

Target Market(s)

We are an online store selling renovation products to home owners are builders. Looking for a classic classy design.

Industry/Entity Type

Home And Garden

Contact Information for Business Card

Maya Torvel
Heritage Hollow
maya@quonbrook.com.au
02 6481 7390
PO Box Glenwarra NSW 2913
www.heritagehollow.com.au

Colors

Designer to choose colors to be used in the design.

Requirements
Must have
• Must include Logo.

```html
<!DOCTYPE html>
<html lang="en">
<head>
<meta charset="utf-8">
<title>Heritage Hollow Business Cards</title>
<link href="https://fonts.googleapis.com/css2?family=Cabin+Sketch:wght@700&family=Patrick+Hand+SC&display=swap" rel="stylesheet">
<style>
  :root {
    --backdrop: #2b2a29;
    --card: #e9e9e9;
    --ink: #1c1c1c;
    --hatch: #3a3a3a;
  }
  html, body { margin: 0; padding: 0; overflow: hidden; }
  body { width: 1177px; height: 1200px; background: var(--backdrop); position: relative; }
  .card { position: absolute; left: 210px; width: 766px; height: 438px; background: var(--card); color: var(--ink); overflow: hidden; }
  .card--front { top: 132px; }
  .card--back { top: 650px; }
  .edge-hatch { position: absolute; top: 0; width: 78px; height: 100%; background: linear-gradient(90deg, #555 0%, #222 40%, #444 70%, #1e1e1e 100%); }
  .edge-hatch--right { right: 0; }
  .edge-hatch--left { left: 0; }
  .brand { position: absolute; border: 1px solid #555; border-radius: 50%; display: flex; align-items: center; justify-content: center; text-align: center; font-family: "Patrick Hand SC", cursive; line-height: 1.05; color: var(--ink); }
  .card--front .brand { left: 38px; top: 84px; width: 232px; height: 232px; font-size: 38px; }
  .card--back .brand { left: 246px; top: -12px; width: 300px; height: 300px; font-size: 50px; }
  .person-name { position: absolute; left: 306px; top: 92px; margin: 0; font-family: "Cabin Sketch", cursive; font-weight: 700; font-size: 50px; letter-spacing: 2px; }
  .stroke { position: absolute; height: 4px; background: var(--ink); border-radius: 3px; transform: rotate(-0.6deg); }
  .card--front .stroke { left: 342px; top: 170px; width: 292px; }
  .card--back .stroke { left: 238px; top: 400px; width: 312px; }
  .contact { position: absolute; left: 320px; display: flex; align-items: center; gap: 18px; font-family: "Patrick Hand SC", cursive; }
  .contact svg { flex: none; }
  .contact--phone { top: 206px; font-size: 32px; letter-spacing: 2px; }
  .contact--mail { top: 279px; font-size: 18px; }
  .contact--web { top: 342px; font-size: 18px; }
  .address { position: absolute; left: 49px; top: 326px; font-family: "Patrick Hand SC", cursive; font-size: 17px; line-height: 1.3; }
  .address svg { display: block; margin: 0 0 6px 93px; }
  .back-phone { position: absolute; left: 238px; top: 338px; width: 312px; text-align: center; font-family: "Patrick Hand SC", cursive; font-size: 44px; letter-spacing: 3px; }
</style>
</head>
<body>
  <section class="card card--front">
    <div class="brand">Heritage<br>Hollow</div>
    <h1 class="person-name">MAYA TORVEL</h1>
    <div class="stroke"></div>
    <div class="contact contact--phone">
      <svg width="24" height="44" viewBox="0 0 24 44"><rect x="2" y="2" width="20" height="40" rx="4" fill="none" stroke="#1c1c1c" stroke-width="3"/><rect x="6" y="8" width="12" height="24" fill="#1c1c1c"/><circle cx="12" cy="37" r="2" fill="#1c1c1c"/></svg>
      <span>02 6481 7390</span>
    </div>
    <div class="contact contact--mail">
      <svg width="36" height="26" viewBox="0 0 36 26"><rect x="1.5" y="1.5" width="33" height="23" fill="none" stroke="#1c1c1c" stroke-width="3"/><path d="M2 2 L18 15 L34 2 M2 24 L14 12 M34 24 L22 12" fill="none" stroke="#1c1c1c" stroke-width="2.5"/></svg>
      <span>MAYA@QUONBROOK.COM.AU</span>
    </div>
    <div class="contact contact--web">
      <svg width="36" height="36" viewBox="0 0 36 36"><circle cx="16" cy="16" r="14" fill="none" stroke="#1c1c1c" stroke-width="3"/><path d="M2 16 H30 M16 2 V30 M6 8 H26 M6 24 H26" stroke="#1c1c1c" stroke-width="2"/><ellipse cx="16" cy="16" rx="7" ry="14" fill="none" stroke="#1c1c1c" stroke-width="2"/><path d="M22 22 L34 28 L28 29 L31 35 L28 36 L25 30 L22 34 Z" fill="#e9e9e9" stroke="#1c1c1c" stroke-width="1.5"/></svg>
      <span>WWW.HERITAGEHOLLOW.COM.AU</span>
    </div>
    <div class="address">
      <svg width="20" height="30" viewBox="0 0 20 30"><path d="M10 29 C4 20 1 15 1 10 A9 9 0 0 1 19 10 C19 15 16 20 10 29 Z" fill="#1c1c1c"/><circle cx="10" cy="10" r="3.5" fill="#e9e9e9"/></svg>
      PO BOX GLENWARRA<br>NSW 2913
    </div>
    <div class="edge-hatch edge-hatch--right" role="img" aria-label="Hand-drawn vertical pen stroke border"></div>
  </section>

  <section class="card card--back">
    <div class="edge-hatch edge-hatch--left" role="img" aria-label="Hand-drawn vertical pen stroke border"></div>
    <div class="brand">Heritage<br>Hollow</div>
    <div class="back-phone">02 6481 7390</div>
    <div class="stroke"></div>
    <div class="edge-hatch edge-hatch--right" role="img" aria-label="Hand-drawn vertical pen stroke border"></div>
  </section>
</body>
</html>
```